Vorlan cards

I am in the auto motive, transportation business I would like a business card that is Something cool, modern edgy, having to do with car culture. I offer towing service for high and exotic cars. I also provide towing for collisions and car accidents. I offer open and enclosed transport nationwide.

Target Market(s)

Car culture people high end auto collectors

Industry/Entity Type

Towing car carrier

Contact Information for Business Card

My company colors black yellow and silver

Font styles to use
Serif

```html
<!DOCTYPE html>
<html lang="en">
<head>
<meta charset="utf-8">
<title>Vorlan Transportation – Business Cards</title>
<link rel="stylesheet" href="https://fonts.googleapis.com/css2?family=Arvo:wght@400;700&display=swap">
<style>
  :root{
    --bg:#b9b9b9;
    --black:#000000;
    --ink:#111111;
    --white:#ffffff;
    --yellow:#f7e04b;
    --rule:#9a9a9a;
    --ghost-a:#050505;
    --ghost-b:#151515;
  }
  *{margin:0;padding:0;box-sizing:border-box}
  html,body{width:1200px;height:1200px;overflow:hidden}
  body{background:var(--bg);position:relative;font-family:"Arvo",Georgia,serif}
  .card{position:absolute;top:303px;height:594px;overflow:hidden}
  .card--back{left:200px;width:370px;background:var(--black)}
  .card--front{left:599px;width:364px;background:var(--white);color:var(--ink);text-align:center}

  .ghost-art{position:absolute;left:0;right:0;top:380px;bottom:0;
    background:linear-gradient(160deg,var(--ghost-b),var(--ghost-a))}

  .brand{position:absolute;left:0;right:0;display:flex;flex-direction:column;align-items:center;gap:10px}
  .brand__mark{width:26px;height:26px;background:var(--yellow)}
  .brand__name{font-weight:700;font-size:30px;line-height:1.05;letter-spacing:1px}
  .brand__sub{font-weight:700;font-size:14px;letter-spacing:2px}
  .card--back .brand{top:250px}
  .card--back .brand__name,.card--back .brand__sub{color:var(--white)}
  .card--front .brand{top:130px}
  .card--front .brand__name,.card--front .brand__sub{color:var(--ink)}

  .back-web{position:absolute;left:0;right:0;top:538px;text-align:center;color:var(--yellow);font-size:14.5px}

  .person{position:absolute;left:0;right:0;top:338px}
  .person__name{font-weight:700;font-size:23px;letter-spacing:.5px;line-height:28px}
  .person__role{font-size:14.5px;line-height:18px}

  .icon-row{position:absolute;left:87px;right:87px;top:396px;display:flex;align-items:center;gap:5px}
  .icon-row__line{flex:1;height:1px;background:var(--rule)}
  .icon{width:25px;height:25px;background:var(--black);border-radius:3px;display:flex;align-items:center;justify-content:center}
  .icon svg{width:19px;height:19px}

  .contact{position:absolute;left:0;right:0;top:428px;font-size:14.5px;line-height:21px}
  .divider{position:absolute;left:88px;right:82px;top:507px;height:1px;background:var(--rule)}
  .address{position:absolute;left:0;right:0;top:520px;font-size:14.5px;line-height:21px}
</style>
</head>
<body>
  <section class="card card--back">
    <div class="ghost-art" role="img" aria-label="Faint dark silhouette of a flatbed tow truck"></div>
    <div class="brand">
      <span class="brand__mark"></span>
      <span class="brand__name">VORLAN</span>
      <span class="brand__sub">TRANSPORTATION</span>
    </div>
    <p class="back-web">www.vorlantransport.com</p>
  </section>

  <section class="card card--front">
    <div class="brand">
      <span class="brand__mark"></span>
      <span class="brand__name">VORLAN</span>
      <span class="brand__sub">TRANSPORTATION</span>
    </div>

    <div class="person">
      <h1 class="person__name">MARCUS HALE</h1>
      <p class="person__role">Managing Director</p>
    </div>

    <div class="icon-row">
      <span class="icon-row__line"></span>
      <span class="icon" aria-label="Phone">
        <svg viewBox="0 0 20 20"><rect x="1" y="1" width="18" height="18" rx="2" fill="#f7e04b"/><path d="M5 8c0-2 2-3 5-3s5 1 5 3h-2.5V7h-5v1z" fill="#000"/><rect x="6" y="9" width="8" height="6" rx="1" fill="#000"/></svg>
      </span>
      <span class="icon" aria-label="Email">
        <svg viewBox="0 0 20 20"><rect x="1" y="1" width="18" height="18" rx="2" fill="#f7e04b"/><rect x="4" y="6" width="12" height="8" fill="none" stroke="#000" stroke-width="1.2"/><path d="M4 6l6 5 6-5M4 14l4.5-4M16 14l-4.5-4" fill="none" stroke="#000" stroke-width="1"/></svg>
      </span>
      <span class="icon" aria-label="Website">
        <svg viewBox="0 0 20 20"><rect x="1" y="1" width="18" height="18" rx="2" fill="#f7e04b"/><circle cx="10" cy="10" r="5.5" fill="#000"/><path d="M8 7l3 1-1 2 2 2-1 2-2-2-2-1z" fill="#f7e04b"/></svg>
      </span>
      <span class="icon-row__line"></span>
    </div>

    <div class="contact">
      <p>044-987 654 321</p>
      <p>info@vorlanmail.com</p>
      <p>www.vorlantransport.com</p>
    </div>
    <div class="divider"></div>
    <div class="address">
      <p>421, Address line goes here</p>
      <p>45452,Country Name</p>
    </div>
  </section>
</body>
</html>
```